Elegant Gildmoor Party Rentals DL flyer

We run a Gildmoor Party Rentals business - this will be used as a business card as well.

our website is gildmoorpartyrentals.com.au

Front page it sour logo which is attached website details - on the front it needs to say wedding and event hire needs etc..

on the back we will have a spot for 4 products but we want to say there is more so check our the website

A background in the flyer only for example like this would be good http://backdropvault.example/dark-texture-image_4417.html

Industry/Entity Type

Wedding

Requirements
Must have
• nice background elegant in style pink and black is the colours

```html
<!DOCTYPE html>
<html lang="en">
<head>
<meta charset="utf-8">
<title>Gildmoor Party Rentals – DL Flyer</title>
<link rel="stylesheet" href="https://fonts.googleapis.com/css2?family=Great+Vibes&display=swap">
<style>
  :root {
    --ink: #111111;
    --panel-dark: #141414;
    --panel-mid: #2a2a2a;
    --script-white: #f2f2f2;
    --brand-pink: #ec3fa6;
    --frame-white: #ffffff;
    --frame-line: #1a1a1a;
    --product-grey: #e6e6e6;
    --product-light: #fbfbfb;
  }
  * { margin: 0; padding: 0; box-sizing: border-box; }
  html, body { width: 1200px; height: 1200px; overflow: hidden; background: var(--ink); }
  .flyer {
    position: relative; width: 1200px; height: 1200px;
    font-family: "Great Vibes", cursive; color: var(--script-white);
  }
  .panel { position: absolute; left: 0; width: 1200px; overflow: hidden; }
  .panel--front { top: 0; height: 594px; }
  .panel--back { top: 600px; height: 600px; }
  .panel__texture {
    position: absolute; inset: 0;
    background: radial-gradient(ellipse at 50% 40%, var(--panel-mid) 0%, var(--panel-dark) 75%);
  }
  .fold-line {
    position: absolute; left: 0; top: 594px; width: 1200px; height: 0;
    border-top: 3px dashed var(--frame-white);
  }
  .script { position: absolute; text-align: center; line-height: 1.65; text-shadow: 0 2px 3px rgba(0,0,0,.6); }
  .front__phone { left: 24px; top: 30px; width: 260px; font-size: 34px; }
  .front__tagline { right: 24px; top: 30px; width: 300px; font-size: 34px; }
  .brand {
    position: absolute; left: 0; width: 1200px;
    display: flex; align-items: center; justify-content: center; gap: 26px;
  }
  .brand__dot { border-radius: 50%; background: var(--brand-pink); flex: none; }
  .brand__name { font-size: 100px; color: var(--script-white); line-height: 1; white-space: nowrap; }
  .front__brand { top: 250px; }
  .front__brand .brand__dot { width: 80px; height: 80px; }
  .front__web { left: 0; top: 520px; width: 1200px; font-size: 40px; line-height: 1; }
  .front__web .dot { color: var(--brand-pink); }
  .back__tagline { left: 20px; top: 40px; width: 300px; font-size: 32px; }
  .back__phone { right: 30px; top: 40px; width: 260px; font-size: 32px; }
  .back__brand { top: 90px; gap: 12px; }
  .back__brand .brand__dot { width: 30px; height: 30px; }
  .back__brand .brand__name { font-size: 38px; }
  .products {
    position: absolute; left: 54px; top: 186px; width: 1092px; height: 300px;
    display: flex; justify-content: space-between;
  }
  .product-frame {
    width: 216px; height: 300px; padding: 14px;
    background: var(--frame-white); border-radius: 22px;
    box-shadow: 0 0 0 5px var(--frame-line), 0 0 0 9px var(--frame-white);
  }
  .product-frame__photo {
    width: 100%; height: 100%; border-radius: 10px;
    background: radial-gradient(circle at 50% 50%, var(--product-grey) 0%, var(--product-light) 70%);
  }
  .back__cta { left: 0; top: 520px; width: 1200px; font-size: 42px; line-height: 1.2; }
</style>
</head>
<body>
<main class="flyer">
  <section class="panel panel--front">
    <div class="panel__texture" role="img" aria-label="Dark black damask textured background"></div>
    <p class="script front__phone">Phone Number:<br>040 555 0182</p>
    <p class="script front__tagline">Wedding and Event<br>Hire Needs!</p>
    <div class="brand front__brand">
      <span class="brand__dot"></span>
      <span class="brand__name">Gildmoor Party Rentals</span>
    </div>
    <p class="script front__web">www<span class="dot">.</span>gildmoorpartyrentals<span class="dot">.</span>com<span class="dot">.</span>au</p>
  </section>

  <div class="fold-line"></div>

  <section class="panel panel--back">
    <div class="panel__texture" role="img" aria-label="Dark black damask textured background"></div>
    <p class="script back__tagline">Wedding and Event<br>Hire Needs!</p>
    <div class="brand back__brand">
      <span class="brand__dot"></span>
      <span class="brand__name">Gildmoor Party Rentals</span>
    </div>
    <p class="script back__phone">Phone Number:<br>040 555 0182</p>
    <div class="products">
      <div class="product-frame"><div class="product-frame__photo" role="img" aria-label="White folding padded wedding chair"></div></div>
      <div class="product-frame"><div class="product-frame__photo" role="img" aria-label="Beige market umbrella on a stand"></div></div>
      <div class="product-frame"><div class="product-frame__photo" role="img" aria-label="Glowing white LED cube seat"></div></div>
      <div class="product-frame"><div class="product-frame__photo" role="img" aria-label="Black bar stool with silver legs"></div></div>
    </div>
    <p class="script back__cta">Check our website for more products!</p>
  </section>
</main>
</body>
</html>
```